Vexo App Form Input Screens - Sleek Clean Design

We have a input form that we would like to transpose into an Vexo App. We have a programmer to do the screens but we need to take this very field heavy form and get it into clean design input screens (We can as many screens as make sense). We want to design to be slick and intuitive. This will be used by young guys who enjoy a gaming atmosphere. But the design has to be easy enough to be completely intuitive to a novice user. The Company likes to do things with Sky Blue colors. Also OK to incorporate burnt orange/yellow (Think glowing sun).

Target Market(s)

18-25 year old males - These guys go door to door and input this data all day

Industry/Entity Type

Solar Energy

Number of Pages Required

5+ page

Font styles to use
Sans Serif

Colors
0355a3
3277b5
85acd3
d0dfed
faa54b
ffc214
f68e4d

Requirements
Must have
• Clean simple sleek Designs - Drop Down Examples. The background and fields have to have distinct colors because these guys will be outside most of the time and if the design is not contrasted enough, it will be hard for them to see.
Nice to have
• Fun ways to incorporate the Glowing Sun Colors (Subtle)
Should not have
• Should not look like Powerpoint

```html
<!DOCTYPE html>
<html lang="en">
<head>
<meta charset="utf-8">
<title>Vexo Solar – Customer Information</title>
<link href="https://fonts.googleapis.com/css2?family=Roboto:wght@400;500&display=swap" rel="stylesheet">
<style>
  :root {
    --sky-deep: #0355a3;
    --sky-mid: #3277b5;
    --sky-soft: #85acd3;
    --sky-pale: #d0dfed;
    --sun-yellow: #ffc214;
    --sun-orange: #faa54b;
    --step-fill: #0d5cb0;
    --step-ring: #1aa3f5;
    --done-fill: #1f9e63;
    --done-ring: #5cc98d;
    --field-border: #2a62a8;
    --text-dark: #2b2b2b;
    --white: #ffffff;
    --go-top: #22b06a;
    --go-bottom: #0d8a4a;
    --back-top: #d4d4d4;
    --back-bottom: #a9a9a9;
  }
  * { box-sizing: border-box; margin: 0; padding: 0; }
  html, body { width: 1200px; height: 900px; overflow: hidden; }
  body { font-family: "Roboto", Arial, sans-serif; position: relative; background: var(--sky-deep); }

  .backdrop {
    position: absolute; inset: 0;
    background:
      linear-gradient(180deg, #0a5fb8 0%, #0a68c6 30%, #1565b8 45%, #0c3f8c 70%, #0a2f78 100%);
  }
  .top-band { position: absolute; left: 0; top: 0; width: 1200px; height: 23px; background: #0a4e9e; }

  .stepper { position: absolute; left: 0; top: 90px; width: 1200px; height: 66px; }
  .stepper-line { position: absolute; left: 80px; right: 80px; top: 31px; height: 4px; background: var(--step-ring); }
  .step {
    position: absolute; top: 0; width: 66px; height: 66px; margin-left: -33px;
    border-radius: 50%; border: 4px solid var(--step-ring); background: var(--step-fill);
    color: var(--white); font-size: 20px; display: flex; align-items: center; justify-content: center;
  }
  .step.done { background: var(--done-fill); border-color: var(--done-ring); }
  .step.current {
    background: var(--white); border-color: var(--sun-yellow); color: var(--text-dark);
    box-shadow: 0 0 14px 3px rgba(255, 194, 20, 0.7);
  }

  .card {
    position: absolute; left: 47px; top: 195px; width: 1106px; height: 498px;
    background: var(--white); border-radius: 4px; overflow: hidden;
    box-shadow: 0 4px 16px rgba(0, 20, 60, 0.4);
  }
  .card-header {
    height: 47px; background: var(--sun-yellow); color: var(--text-dark);
    font-size: 20px; text-align: center; line-height: 47px; word-spacing: 6px;
  }
  .field-label { position: absolute; font-size: 20px; color: var(--text-dark); }
  .field-input {
    position: absolute; height: 48px; width: 518px;
    border: 1.5px solid var(--field-border); border-radius: 4px; background: var(--white);
    box-shadow: inset 0 3px 5px rgba(0, 0, 0, 0.12);
  }
  .col-left { left: 21px; }
  .col-right { left: 565px; }
  .field-input.narrow { width: 366px; }
  .check-box {
    position: absolute; left: 399px; top: 334px; width: 37px; height: 37px;
    border: 1.5px solid var(--field-border); border-radius: 4px; background: var(--white);
    display: flex; align-items: center; justify-content: center;
  }
  .check-label { position: absolute; left: 445px; top: 341px; font-size: 20px; color: var(--text-dark); }

  .card-divider { position: absolute; left: 0; right: 0; top: 423px; height: 1px; background: #c8c8c8; }
  .btn {
    position: absolute; top: 435px; height: 49px; border-radius: 3px;
    font-size: 20px; display: flex; align-items: center; justify-content: center;
  }
  .btn-previous {
    left: 22px; width: 130px; color: #555;
    background: linear-gradient(180deg, var(--back-top), var(--back-bottom)); border: 1px solid #9a9a9a;
  }
  .btn-next {
    left: 963px; width: 119px; color: var(--white);
    background: linear-gradient(180deg, var(--go-top), var(--go-bottom)); border: 1px solid #0b7a40;
  }
</style>
</head>
<body>
  <div class="backdrop" role="img" aria-label="Rooftop covered with rows of solar panels under a blue sky"></div>
  <div class="top-band"></div>

  <nav class="stepper" aria-label="Form progress">
    <div class="stepper-line"></div>
    <div class="step done" style="left:80px">1</div>
    <div class="step current" style="left:195px">2</div>
    <div class="step" style="left:309px">3</div>
    <div class="step" style="left:424px">4</div>
    <div class="step" style="left:539px">5</div>
    <div class="step" style="left:655px">6</div>
    <div class="step" style="left:770px">7</div>
    <div class="step" style="left:885px">8</div>
    <div class="step" style="left:1001px">9</div>
    <div class="step" style="left:1116px">10</div>
  </nav>

  <section class="card">
    <header class="card-header">CUSTOMER INFORMATION</header>

    <label class="field-label col-left" style="top:76px">Who Passed&nbsp; Credit?</label>
    <div class="field-input col-left" style="top:108px"></div>
    <label class="field-label col-right" style="top:76px">E Mail</label>
    <div class="field-input col-right" style="top:108px"></div>

    <label class="field-label col-left" style="top:187px">Name asit Appears on Electric Bill</label>
    <div class="field-input col-left" style="top:219px"></div>
    <label class="field-label col-right" style="top:187px">Home Phone</label>
    <div class="field-input col-right" style="top:219px"></div>

    <label class="field-label col-left" style="top:295px">Primary Owner (Full Name)</label>
    <div class="field-input col-left narrow" style="top:328px"></div>
    <div class="check-box">
      <svg width="24" height="20" viewBox="0 0 24 20"><path d="M2 10 L9 17 L22 3" fill="none" stroke="#2a62a8" stroke-width="3.5" stroke-linecap="round" stroke-linejoin="round"/></svg>
    </div>
    <span class="check-label">On Title</span>
    <label class="field-label col-right" style="top:295px">Cell Phone</label>
    <div class="field-input col-right" style="top:328px"></div>

    <div class="card-divider"></div>
    <div class="btn btn-previous">Previous</div>
    <div class="btn btn-next">Next</div>
  </section>
</body>
</html>
```